Business Card for Freelance Copywriting & Web Design Business

Hi! I have a logo but want a new business card. Here's a better idea of what I'm thinking:
-Brand new double-sided business card, rounded cards, embossed logo, nice quality paper
-Include phone (604-382-5194), email (hello@lauraberndt.org), and website (www.lauraberndt.org). No address, please, since I service clients worldwide.
-I'd like the fonts to match those on my website (www.lauraberndt.org). I had to purchase the one font (Born Ready), attached. I'm not sure which version was used on my site so I included all that I purchased. The secondary font is Helvetica
-I'd also like the tagline "Powerful Words. Impressive Results." included.
-My primary brand colour is the teal, colour #19ADC3
Laura Berndt | Laura Berndt Copywriting & Web Design <hello@lauraberndt.org>
-I'd also like the following services listed on the new cards:
SEO Website Content
SEO Blog Content
SEO Website Design
Contact Information for Business Card
as stated in brief
Font styles to use
Other font styles liked:
- See brief
Look and feel
Each slider illustrates characteristics of the customer's brand and the style your logo design should communicate.

```html
<!DOCTYPE html>
<html lang="en">
<head>
<meta charset="utf-8">
<title>Laura Berndt Copywriting &amp; Web Design – Business Card</title>
<link rel="stylesheet" href="https://fonts.googleapis.com/css2?family=Arimo:wght@400;700&display=swap">
<style>
  :root {
    --backdrop: #2b2b2c;
    --card-black: #0d0d0e;
    --card-white: #ffffff;
    --ink: #111111;
    --ink-soft: #333333;
    --teal: #19adc3;
    --teal-edge: #8fc8d2;
    --teal-dot: #86c3cf;
    --feather-black: #3a3a3c;
    --feather-teal: #a9d6df;
    --reverse-text: #ffffff;
  }
  * { margin: 0; padding: 0; box-sizing: border-box; }
  html, body {
    width: 1200px;
    height: 1186px;
    overflow: hidden;
    background: var(--backdrop);
    font-family: "Arimo", Helvetica, Arial, sans-serif;
  }
  .card-set {
    position: relative;
    width: 1200px;
    height: 1186px;
  }
  .card {
    position: absolute;
    left: 250px;
    width: 700px;
    height: 400px;
    border-radius: 14px;
    overflow: hidden;
    box-shadow: 0 0 0 4px var(--teal-edge), 0 18px 40px rgba(0,0,0,0.45);
  }

  /* Front */
  .card--front {
    top: 150px;
    background: var(--card-black);
  }
  .front-decoration {
    position: absolute;
    right: 40px;
    top: -40px;
    width: 440px;
    height: 420px;
    border-radius: 50%;
    background: radial-gradient(ellipse at 55% 40%, var(--feather-black) 0%, rgba(40,40,42,0.5) 45%, rgba(13,13,14,0) 72%);
  }
  .front-brand {
    position: absolute;
    left: 90px;
    top: 150px;
    color: var(--reverse-text);
    font-weight: 400;
  }
  .front-brand .brand-name {
    display: block;
    font-size: 64px;
    line-height: 1;
    letter-spacing: 0.5px;
  }
  .front-brand .brand-line {
    display: block;
    margin-top: 18px;
    font-size: 20px;
    letter-spacing: 4px;
    text-transform: uppercase;
  }

  /* Back */
  .card--back {
    top: 630px;
    background: var(--card-white);
  }
  .back-decoration {
    position: absolute;
    left: 150px;
    top: 120px;
    width: 170px;
    height: 150px;
    border-radius: 50%;
    background: radial-gradient(ellipse at center, var(--feather-teal) 0%, rgba(169,214,223,0.35) 50%, rgba(255,255,255,0) 75%);
  }
  .back-brand {
    position: absolute;
    left: 60px;
    top: 170px;
    color: var(--ink);
    font-weight: 400;
  }
  .back-brand .brand-name {
    display: block;
    font-size: 40px;
    line-height: 1;
  }
  .back-brand .brand-line {
    display: block;
    margin-top: 10px;
    font-size: 12.5px;
    letter-spacing: 2.6px;
    text-transform: uppercase;
  }
  .contact {
    position: absolute;
    left: 400px;
    top: 52px;
    color: var(--ink);
  }
  .contact .person-name {
    font-size: 27px;
    font-weight: 700;
    line-height: 1.05;
  }
  .contact .person-role {
    font-size: 14px;
    color: var(--ink-soft);
    margin: 2px 0 0 22px;
  }
  .contact-list {
    list-style: none;
    margin: 10px 0 0 48px;
  }
  .contact-list li {
    display: flex;
    align-items: center;
    gap: 9px;
    font-size: 15px;
    line-height: 24px;
  }
  .contact-list svg { width: 13px; height: 13px; flex: none; }
  .services {
    position: absolute;
    left: 0;
    right: 0;
    bottom: 48px;
    display: flex;
    justify-content: center;
    gap: 34px;
    list-style: none;
  }
  .services li {
    display: flex;
    align-items: center;
    gap: 7px;
    font-size: 17px;
    color: var(--ink);
  }
  .services li::before {
    content: "";
    width: 8px;
    height: 8px;
    border-radius: 50%;
    background: var(--teal-dot);
  }
</style>
</head>
<body>
<main class="card-set">

  <section class="card card--front" aria-label="Card front">
    <div class="front-decoration" role="img" aria-label="Large dark feather illustration"></div>
    <div class="front-brand">
      <span class="brand-name">Laura Berndt</span>
      <span class="brand-line">Copywriting &amp; Web Design</span>
    </div>
  </section>

  <section class="card card--back" aria-label="Card back">
    <div class="back-decoration" role="img" aria-label="Light teal feather illustration"></div>
    <div class="back-brand">
      <span class="brand-name">Laura Berndt</span>
      <span class="brand-line">Copywriting &amp; Web Design</span>
    </div>

    <div class="contact">
      <p class="person-name">Laura Berndt</p>
      <p class="person-role">Managing Director</p>
      <ul class="contact-list">
        <li>
          <svg viewBox="0 0 16 16" aria-hidden="true"><path fill="#111" d="M3.6 1.2l2.2 2.6-1.3 1.8c.9 2 2.6 3.7 4.6 4.6l1.8-1.3 2.6 2.2-1.2 2.6C7.4 13.3 2.7 8.6 1 3.6z"/></svg>
          604-382-5194
        </li>
        <li>
          <svg viewBox="0 0 16 16" aria-hidden="true"><rect x="1" y="3" width="14" height="10" rx="1" fill="#111"/><path d="M1.5 3.5L8 9l6.5-5.5" stroke="#fff" stroke-width="1.4" fill="none"/></svg>
          hello@lauraberndt.org
        </li>
        <li>
          <svg viewBox="0 0 16 16" aria-hidden="true"><circle cx="8" cy="8" r="6.5" fill="none" stroke="#111" stroke-width="1.6"/><ellipse cx="8" cy="8" rx="2.8" ry="6.5" fill="none" stroke="#111" stroke-width="1.2"/><path d="M1.5 8h13" stroke="#111" stroke-width="1.2"/></svg>
          www.lauraberndt.org
        </li>
      </ul>
    </div>

    <ul class="services">
      <li>SEO Website Content</li>
      <li>SEO Blog Content</li>
      <li>SEO Website Design</li>
    </ul>
  </section>

</main>
</body>
</html>
```